Website design for learning and development business

I need a logo for my new business based in Australasia. I am a kiwi who is a creative change maker working in the Learning & development space. I design experiential learning opportunities for businesses to grow and nurture their tribes. I take a holistic look at an organisation and analyse what is needed to build a positive culture with a growth mindset woven into their DNA. I would like to see designs that are based on the following word snaps - creative, interesting, tribal, journey, adaptability, engaging, fluid, architectural, bespoke, courageous, challenging .I have the logo (attached) and I Need a startup business website designed. I am a Learning and development professional who is looking at going out on my own and establishing my own business. I would like a website designed that people would go to to check out what I do, how I do, what skills I have and how to contact me. Also room for a blog/articles.

Target Market(s)

Small to medium business

Industry/Entity Type

Self employed training and consultancy company

Number of Pages Required

5+ page

Requirements
Must have
• home page, about page, contact us page, blog page, search for us page
Nice to have
• Testimonials,

```html
<!DOCTYPE html>
<html lang="en">
<head>
<meta charset="utf-8">
<title>Veridian Consulting — Learning &amp; Development</title>
<link href="https://fonts.googleapis.com/css2?family=Saira+Semi+Condensed:wght@500;600;700&family=Open+Sans:wght@400;600;700&display=swap" rel="stylesheet">
<style>
  :root{
    --forest:#0f3a22;
    --forest-deep:#07200f;
    --cyan:#00f0f4;
    --white:#ffffff;
    --ink:#1e1e1e;
    --muted:#555555;
    --yellow:#fdd623;
    --green:#3bb53b;
    --orange:#f06a2c;
    --red:#e11d2a;
    --navy:#2a2f86;
    --sky:#3c8fd6;
    --olive:#c9c21a;
    --leaf:#1f9a3a;
    --paper:#f1f1f1;
    --black:#000000;
  }
  *{box-sizing:border-box;margin:0;padding:0}
  html,body{width:1200px;height:5052px;overflow:hidden;background:var(--white)}
  body{font-family:"Open Sans",Arial,sans-serif;color:var(--ink)}
  .page{position:relative;width:1200px;height:5052px;overflow:hidden}
  .abs{position:absolute}
  .heading{font-family:"Saira Semi Condensed","Arial Narrow",sans-serif;font-weight:700;text-transform:uppercase;color:var(--ink)}

  /* Hero */
  .hero{left:0;top:0;width:1200px;height:780px;background:radial-gradient(ellipse at 60% 40%,#1f5a33 0%,var(--forest) 45%,var(--forest-deep) 100%)}
  .brand{left:172px;top:92px;width:300px;font-family:"Saira Semi Condensed","Arial Narrow",sans-serif;font-weight:700;font-size:24px;line-height:28px;color:var(--white);letter-spacing:1px;white-space:nowrap}
  .nav{left:551px;top:72px;display:flex;gap:26px;font-size:14px;font-weight:700;color:var(--white)}
  .nav span{line-height:20px}
  .search-btn{left:890px;top:53px;width:136px;height:55px;background:var(--cyan);border-radius:5px;color:#0c3a2a;font-size:14px;font-weight:700;display:flex;align-items:center;justify-content:center}
  .hero-title{left:170px;top:240px;font-size:54px;line-height:68px;color:var(--white)}
  .hero-photo{left:560px;top:135px;width:640px;height:455px;border-radius:48% 52% 40% 60%/50% 45% 55% 50%;background:radial-gradient(ellipse at 45% 45%,#c9d43a 0%,#7fa832 40%,rgba(31,90,51,0) 72%)}
  .hero-wave{left:0;top:600px}

  /* What I do */
  .what-title{left:0;top:876px;width:1200px;text-align:center;font-size:36px}
  .service{top:977px;width:275px;height:313px;border-radius:10px;overflow:hidden;background:var(--yellow)}
  .service .photo{height:229px}
  .service .label{height:84px;display:flex;align-items:center;justify-content:center;text-align:center;font-family:"Saira Semi Condensed","Arial Narrow",sans-serif;font-weight:700;font-size:19px;line-height:22px;text-transform:uppercase;color:var(--ink)}

  /* How I do */
  .how{left:0;top:1304px;width:1200px;height:867px;background:
      radial-gradient(ellipse at 72% 40%,#f7e2a6 0%,#d8b06a 25%,rgba(120,100,70,0) 60%),
      linear-gradient(180deg,rgba(0,0,0,0) 55%,#2d2a1e 100%),
      linear-gradient(90deg,#2f3034 0%,#4f4b44 40%,#a48b5f 70%,#c9a567 100%)}
  .how-title{left:170px;top:1670px;font-size:36px;color:var(--white)}
  .how-copy{left:172px;top:1738px;width:370px;font-size:13px;line-height:27px;color:#e8e4da;text-align:justify}
  .read-btn{left:172px;top:1961px;width:109px;height:55px;background:var(--green);border-radius:8px;color:var(--white);font-size:13px;font-weight:700;display:flex;align-items:center;justify-content:center}

  /* Skills */
  .skills-title{left:102px;top:2575px;transform:translate(-50%,-50%) rotate(-90deg);transform-origin:center;font-size:36px;white-space:nowrap}
  .skill{text-align:right;white-space:nowrap}
  .skill h3{font-family:"Open Sans",Arial,sans-serif;font-weight:400;font-size:24px;line-height:30px;color:var(--ink);text-transform:uppercase}
  .skill p{font-size:14px;line-height:20px;color:var(--muted)}
  .illustration{left:588px;top:2440px;width:470px;height:365px;border-radius:40% 60% 50% 50%/55% 50% 50% 45%;background:radial-gradient(ellipse at 50% 40%,#f0c21e 0%,#e0342c 35%,#2b9a3a 65%,rgba(255,255,255,0) 75%);opacity:.55}

  /* Blog */
  .blog{left:0;top:2940px;width:1200px;height:894px;background:linear-gradient(180deg,#ffffff 0%,var(--paper) 30%,#e9eaec 70%,#ffffff 100%)}
  .blog-title{left:0;top:3060px;width:1200px;text-align:center;font-size:36px}
  .card{background:var(--white);border-radius:8px;overflow:hidden;box-shadow:0 4px 14px rgba(0,0,0,.15)}
  .big-card{left:172px;top:3190px;width:554px;height:516px}
  .big-card .photo{height:410px;background:linear-gradient(135deg,#e9e5e2 0%,#c7c0bb 35%,#6d7d95 70%,#c9d0db 100%)}
  .big-card .meta{display:flex;padding:22px 20px 0 20px;gap:18px}
  .date{font-family:"Saira Semi Condensed","Arial Narrow",sans-serif;text-align:center;color:var(--ink)}
  .date .m{font-size:17px;font-weight:600;line-height:18px}
  .date .d{font-size:34px;font-weight:700;line-height:36px}
  .post-title{font-size:14px;font-weight:700;text-transform:uppercase;line-height:20px}
  .post-text{font-size:12px;line-height:20px;color:var(--muted);margin-top:4px}
  .small-card{left:751px;width:275px;height:243px}
  .small-card .photo{height:168px}
  .small-card .foot{display:flex;align-items:center;justify-content:space-between;padding:14px 16px 0 14px}
  .small-card .post-title{font-size:13px;line-height:20px;width:190px}

  /* Testimonials */
  .test-title{left:0;top:3960px;width:1200px;text-align:center;font-size:36px}
  .quote{top:4132px;width:410px;height:290px;text-align:center;padding-top:96px}
  .quote h4{font-family:"Saira Semi Condensed","Arial Narrow",sans-serif;font-weight:700;font-size:24px;text-transform:uppercase;color:var(--ink)}
  .quote p{font-size:12px;line-height:20px;color:var(--muted);padding:12px 18px 0}
  .quote .who{font-size:12px;color:var(--ink);padding-top:18px}
  .avatar{top:4078px;width:112px;height:112px;border-radius:50%;border:3px solid var(--red);background:linear-gradient(180deg,#d9d9d9,#9a9a9a)}

  /* Footer */
  .footer{left:0;top:4520px;width:1200px;height:532px;background:var(--black)}
  .contact-title{left:170px;top:4632px;font-size:28px;color:var(--white)}
  .field{left:172px;width:268px;height:55px;background:var(--white);border-radius:8px;font-size:13px;color:#444;padding:0 12px;display:flex;align-items:center}
  .submit{left:172px;top:4824px;width:116px;height:56px;background:var(--green);border-radius:8px;color:var(--white);font-size:15px;font-weight:600;display:flex;align-items:center;justify-content:center}
  .footer-brand{left:569px;top:4790px;width:460px;text-align:center;font-family:"Saira Semi Condensed","Arial Narrow",sans-serif;font-weight:700;font-size:46px;line-height:50px;color:var(--white);letter-spacing:2px}
  .rule{left:172px;top:4956px;width:854px;height:1px;background:#555}
  .copyright{left:0;top:4994px;width:1200px;text-align:center;font-size:12px;font-weight:600;color:var(--white)}
</style>
</head>
<body>
<div class="page">

  <!-- Hero -->
  <section class="abs hero"></section>
  <div class="abs hero-photo" role="img" aria-label="Photograph of a colourful chameleon perched on a branch"></div>
  <div class="abs brand">VERIDIAN CONSULTING</div>
  <nav class="abs nav"><span>HOME</span><span>ABOUT</span><span>CONTACT US</span><span>BLOG</span></nav>
  <div class="abs search-btn">SEARCH FOR US</div>
  <h1 class="abs heading hero-title">Learning &amp;<br>Development<br>Professional</h1>
  <svg class="abs hero-wave" width="1200" height="190" viewBox="0 0 1200 190">
    <path d="M0,80 C120,20 260,10 420,50 C600,95 760,130 1200,110 L1200,190 L0,190 Z" fill="var(--cyan)"/>
    <path d="M0,150 C140,90 300,60 480,95 C660,130 840,160 1000,140 C1080,130 1150,110 1200,100 L1200,190 L0,190 Z" fill="var(--white)"/>
  </svg>

  <!-- What I do -->
  <h2 class="abs heading what-title">What I Do</h2>
  <article class="abs service" style="left:172px">
    <div class="photo" role="img" aria-label="Photo of a team at a customer service training session" style="background:linear-gradient(135deg,#cfcac4,#7b7a7e 55%,#3b3d44)"></div>
    <div class="label">Customer Service<br>Training</div>
  </article>
  <article class="abs service" style="left:463px">
    <div class="photo" role="img" aria-label="Photo of colleagues in a supportive conversation" style="background:linear-gradient(135deg,#e7e3dd,#b49a6e 55%,#5c4e3f)"></div>
    <div class="label">Mental Health<br>Awareness</div>
  </article>
  <article class="abs service" style="left:751px">
    <div class="photo" role="img" aria-label="Photo of support staff with headsets at a desk" style="background:linear-gradient(135deg,#eef0f2,#9db4cc 55%,#4c5b6e)"></div>
    <div class="label">Policy<br>Training</div>
  </article>

  <!-- How I do -->
  <section class="abs how" role="img" aria-label="Photo of a person standing in a meadow at sunset with birds flying"></section>
  <svg class="abs" style="left:0;top:1304px" width="1200" height="300" viewBox="0 0 1200 300">
    <path d="M0,0 H1200 V140 C1080,125 950,150 820,215 C720,265 600,265 520,205 C420,130 330,35 200,15 C120,3 50,6 0,16 Z" fill="var(--white)"/>
  </svg>
  <h2 class="abs heading how-title">How I Do</h2>
  <p class="abs how-copy">Nam libero tempore, cum soluta nobis est eligendi optio cumque nihil impedit quo minus id quod maxime placeat facere possimus, omnis voluptas assumenda est, omnis dolor repellendus. Temporibus autem quibusdam et aut officiis debitis aut rerum necessitatibus saepe eveniet ut et voluptates repudiandae sint et molestiae non recusandae. Itaque earum rerum hic tenetur.</p>
  <div class="abs read-btn">READ MORE</div>

  <!-- Skills -->
  <h2 class="abs heading skills-title">What Skills I Have</h2>
  <div class="abs illustration" role="img" aria-label="Colourful illustrated chameleon on a curling green branch"></div>
  <svg class="abs" style="left:0;top:2171px" width="1200" height="769" viewBox="0 0 1200 769">
    <path d="M804,70 C640,80 520,240 512,417 C505,590 640,730 804,737" fill="none" stroke="var(--green)" stroke-width="7" stroke-linecap="round"/>
    <g stroke="var(--white)" stroke-width="3" fill="none" stroke-linecap="round">
      <circle cx="610" cy="149" r="37" fill="var(--orange)" stroke="none"/>
      <circle cx="610" cy="152" r="12"/><path d="M604,152 l4,4 l8,-8 M610,128 v-6 M592,136 l-4,-4 M628,136 l4,-4"/>
      <circle cx="545" cy="247" r="37" fill="var(--red)" stroke="none"/>
      <rect x="528" y="233" width="34" height="24" rx="6"/><path d="M536,257 l-4,8 l10,-8"/>
      <circle cx="510" cy="353" r="37" fill="var(--navy)" stroke="none"/>
      <circle cx="510" cy="350" r="6"/><path d="M498,370 a12,12 0 0 1 24,0 M492,350 l-6,-12 M528,350 l6,-12 M510,332 v-8"/>
      <circle cx="516" cy="467" r="37" fill="var(--sky)" stroke="none"/>
      <path d="M506,470 c-8,-8 -8,-22 4,-22 c12,0 12,14 -4,22 Z M522,484 c-5,-5 -5,-12 2,-12 c7,0 7,7 -2,12"/>
      <circle cx="549" cy="571" r="37" fill="var(--olive)" stroke="none"/>
      <rect x="533" y="555" width="32" height="32" rx="4"/><path d="M540,571 h18 M553,566 l5,5 l-5,5 M545,566 l-5,5 l5,5"/>
      <circle cx="623" cy="667" r="37" fill="var(--leaf)" stroke="none"/>
      <rect x="606" y="652" width="34" height="24" rx="3"/><path d="M615,684 h16 M623,676 v8"/><circle cx="623" cy="664" r="5"/>
    </g>
  </svg>
  <div class="abs skill" style="right:645px;top:2290px"><h3>Creative</h3><p>Nam libero tempore, cum soluta nobis</p></div>
  <div class="abs skill" style="right:712px;top:2388px"><h3>Interesting</h3><p>Nam libero tempore, cum soluta nobis</p></div>
  <div class="abs skill" style="right:745px;top:2494px"><h3>Tribal</h3><p>Nam libero tempore, cum soluta nobis</p></div>
  <div class="abs skill" style="right:738px;top:2607px"><h3>Journey</h3><p>Nam libero tempore, cum soluta nobis</p></div>
  <div class="abs skill" style="right:706px;top:2712px"><h3>Adaptability</h3><p>Nam libero tempore, cum soluta nobis</p></div>
  <div class="abs skill" style="right:632px;top:2809px"><h3>Engaging</h3><p>Nam libero tempore, cum soluta nobis</p></div>

  <!-- Blog -->
  <section class="abs blog"></section>
  <h2 class="abs heading blog-title">Blog &amp; Articles</h2>
  <article class="abs card big-card">
    <div class="photo" role="img" aria-label="Photo of smiling call centre staff wearing headsets"></div>
    <div class="meta">
      <div class="date"><div class="m">MAR</div><div class="d">20</div></div>
      <div>
        <div class="post-title">Sed ut perspiciatis unde omnis iste natus</div>
        <div class="post-text">Nemo enim ipsam voluptatem quia voluptas sit aspernatur aut odit aut fugit, sed quia conse quuntur magni dolores</div>
      </div>
    </div>
  </article>
  <article class="abs card small-card" style="top:3190px">
    <div class="photo" role="img" aria-label="Photo of colleagues reviewing work on a tablet" style="background:linear-gradient(135deg,#eef1f4,#a9b6c6 55%,#55637a)"></div>
    <div class="foot"><div class="post-title">Sed ut perspiciatis unde omnis iste natus</div>
      <svg width="14" height="34" viewBox="0 0 14 34"><path d="M2,2 L12,17 L2,32" fill="none" stroke="var(--ink)" stroke-width="2"/></svg></div>
  </article>
  <article class="abs card small-card" style="top:3457px">
    <div class="photo" role="img" aria-label="Photo of a team working together at computers" style="background:linear-gradient(135deg,#dde3e8,#8f9aa6 55%,#3f4752)"></div>
    <div class="foot"><div class="post-title">Sed ut perspiciatis unde omnis iste natus</div>
      <svg width="14" height="34" viewBox="0 0 14 34"><path d="M2,2 L12,17 L2,32" fill="none" stroke="var(--ink)" stroke-width="2"/></svg></div>
  </article>

  <!-- Testimonials -->
  <h2 class="abs heading test-title">Tesimonials</h2>
  <svg class="abs" style="left:74px;top:4248px" width="32" height="56" viewBox="0 0 32 56"><path d="M28,2 L4,28 L28,54" fill="none" stroke="var(--ink)" stroke-width="2.5"/></svg>
  <svg class="abs" style="left:1098px;top:4248px" width="32" height="56" viewBox="0 0 32 56"><path d="M4,2 L28,28 L4,54" fill="none" stroke="var(--ink)" stroke-width="2.5"/></svg>
  <article class="abs card quote" style="left:172px">
    <h4>Great Work</h4>
    <p>Nemo enim ipsam voluptatem quia voluptas sit aspernatur aut odit aut fugit, sed quia conse quuntur magni dolores. Nemo enim ipsam voluptatem quia voluptas sit aspernatur aut odit aut fugit, sed quia conse quuntur magni dolores.</p>
    <div class="who">- Tom Harlow</div>
  </article>
  <article class="abs card quote" style="left:616px">
    <h4>Good Service</h4>
    <p>Nemo enim ipsam voluptatem quia voluptas sit aspernatur aut odit aut fugit, sed quia conse quuntur magni dolores. Nemo enim ipsam voluptatem quia voluptas sit aspernatur aut odit aut fugit, sed quia conse quuntur magni dolores.</p>
    <div class="who">- Mira</div>
  </article>
  <div class="abs avatar" style="left:321px" role="img" aria-label="Portrait photo of the client"></div>
  <div class="abs avatar" style="left:765px" role="img" aria-label="Portrait photo of the client"></div>

  <!-- Footer -->
  <footer class="abs footer"></footer>
  <h2 class="abs heading contact-title">Contact Us</h2>
  <div class="abs field" style="top:4691px">Name</div>
  <div class="abs field" style="top:4757px">Phone</div>
  <div class="abs submit">SUBMIT</div>
  <div class="abs footer-brand">VERIDIAN<br>CONSULTING</div>
  <div class="abs rule"></div>
  <div class="abs copyright">COPYRIGHTS 2021 VERIDIAN.</div>

</div>
</body>
</html>
```